Business card for marketing analytics company

Need a business card for new company. I have a logo already that I want to be built into the card and should use those colours

Company is called steered by tallies
Design must bring steered by tallies to life not be a card that could be for anyone with a logo put on it.

Like the front to be fairly clean and uncluttered bringing the logo out with a suitable design on the back of the card.

The logo represents a compass and business growth so those themes along with numbers, analytics , data are appropriate.
I'm often working with creative industries so also needs to reflect the creative side of analytics rather than be very corporate looking.

Target Market(s)

Ad agency, media agency, consumer goods clients

Industry/Entity Type

Market Research

Contact Information for Business Card

Needs to include name, title, email and phone number

Colors
f78f20
f68d4d
ec1f27

Requirements
Must have
• Must bring steered by tallies to life not be a card that could be for anyone with a logo put on it.
• Logo, Correct colours
• Like a design on the back that relates to company name
• Designs for both sides
Should not have
• Please do not just submit logo and a coloured card.
• It needs to have a design element to it
• No black background
• No clear cards - needs front & back

```html
<!DOCTYPE html>
<html lang="en">
<head>
<meta charset="utf-8">
<title>Ferncliff Metrics – Business Card</title>
<link rel="stylesheet" href="https://fonts.googleapis.com/css2?family=Source+Sans+3:wght@400;600&display=swap">
<style>
  :root {
    --backdrop: #9a9a9a;
    --card-light: #f1f2f1;
    --card-shade: #dcdddf;
    --grid-line: rgba(170, 195, 190, 0.22);
    --red: #c01f28;
    --orange: #f27127;
    --slate: #525c63;
    --blue: #7299cf;
    --white: #ffffff;
    --ink: #1f1f1f;
  }
  * { margin: 0; padding: 0; box-sizing: border-box; }
  html, body {
    width: 1200px;
    height: 1200px;
    overflow: hidden;
    background: var(--backdrop);
    font-family: "Source Sans 3", sans-serif;
  }
  .canvas { position: relative; width: 1200px; height: 1200px; }
  .card {
    position: absolute;
    width: 850px;
    height: 520px;
    background:
      linear-gradient(var(--grid-line) 1px, transparent 1px) 0 0 / 12px 12px,
      linear-gradient(90deg, var(--grid-line) 1px, transparent 1px) 0 0 / 12px 12px,
      linear-gradient(110deg, var(--card-shade) 0%, var(--card-light) 45%, var(--card-shade) 75%, var(--card-light) 100%);
  }
  .card svg { display: block; width: 100%; height: 100%; }
  .card--front { left: 42px; top: 38px; }
  .card--back { left: 274px; top: 626px; }
  .wordmark { font-weight: 600; fill: var(--slate); font-size: 40px; }
  .pie-label { fill: var(--white); }
  .contact-email { fill: var(--blue); font-size: 38px; }
  .contact-phone { fill: var(--white); font-size: 41px; }
  .bar-label { fill: var(--white); font-size: 40px; }
  .axis-title { fill: var(--ink); font-size: 40px; }
</style>
</head>
<body>
<main class="canvas">

  <section class="card card--front" aria-label="Card front">
    <svg viewBox="0 0 1062 649" xmlns="http://www.w3.org/2000/svg">
      <text class="wordmark" x="58" y="128">Ferncliff Metrics</text>

      <g class="contact-pie" stroke="var(--blue)" stroke-width="3" stroke-linejoin="round">
        <path class="slice slice--name" fill="var(--red)" d="M738 334 L556.3 152.3 A257 257 0 0 1 991.8 293.8 Z"/>
        <path class="slice slice--title" fill="var(--orange)" d="M738 334 L991.8 293.8 A257 257 0 0 1 951.1 477.7 Z"/>
        <path class="slice slice--phone" fill="var(--slate)" d="M738 334 L951.1 477.7 A257 257 0 0 1 579.8 536.5 Z"/>
        <path class="slice slice--email" fill="var(--white)" d="M738 334 L579.8 536.5 A257 257 0 0 1 556.3 152.3 Z"/>
        <circle cx="738" cy="334" r="257" fill="none" stroke-width="8"/>
      </g>

      <text class="pie-label" x="786" y="182" font-size="58" text-anchor="middle" transform="rotate(10 786 182)">Name</text>
      <text class="pie-label" x="893" y="376" font-size="38" text-anchor="middle" transform="rotate(10 893 370)">Job Title</text>

      <g class="contact-email" text-anchor="middle">
        <text x="573" y="296">abc</text>
        <text x="573" y="345">@email</text>
        <text x="573" y="394">.com</text>
      </g>
      <g class="icon-envelope" fill="none" stroke="var(--blue)" stroke-width="3">
        <rect x="659" y="319" width="44" height="29"/>
        <path d="M659 319 L681 341 L703 319"/>
      </g>

      <g class="icon-phone" fill="none" stroke="var(--white)" stroke-width="3">
        <rect x="736" y="365" width="22" height="42" rx="2"/>
        <line x1="736" y1="400" x2="758" y2="400" stroke-width="5"/>
      </g>
      <g class="contact-phone" text-anchor="middle">
        <text x="744" y="452">+00</text>
        <text x="744" y="501">00 00</text>
        <text x="744" y="550">000 000</text>
      </g>
    </svg>
  </section>

  <section class="card card--back" aria-label="Card back">
    <svg viewBox="0 0 1062 649" xmlns="http://www.w3.org/2000/svg">
      <g class="bars">
        <rect x="227" y="336" width="67" height="224" fill="var(--red)"/>
        <rect x="365" y="269" width="67" height="291" fill="var(--orange)"/>
        <rect x="503" y="235" width="67" height="325" fill="var(--slate)"/>
        <rect x="630" y="182" width="67" height="378" fill="var(--red)"/>
        <rect x="757" y="153" width="67" height="407" fill="var(--orange)"/>
        <rect x="874" y="111" width="67" height="449" fill="var(--slate)"/>
      </g>
      <g class="bar-labels">
        <text class="bar-label" transform="translate(274 524) rotate(-90)">Service 1</text>
        <text class="bar-label" transform="translate(412 524) rotate(-90)">Service 2</text>
        <text class="bar-label" transform="translate(550 524) rotate(-90)">Service 3</text>
        <text class="bar-label" transform="translate(677 524) rotate(-90)">Service 4</text>
        <text class="bar-label" transform="translate(804 524) rotate(-90)">Service 5</text>
        <text class="bar-label" transform="translate(921 524) rotate(-90)">Service 6</text>
      </g>
      <polyline class="trend-line" fill="none" stroke="var(--blue)" stroke-width="3"
        points="262,336 398,268 536,235 666,182 788,153 908,111"/>
      <g class="axes" stroke="var(--blue)" stroke-width="3" fill="none">
        <path d="M111 96 L111 560 L993 560"/>
      </g>
      <text class="axis-title" text-anchor="middle" transform="translate(88 335) rotate(-90)">Business Growth</text>
      <text class="axis-title" x="572" y="611" text-anchor="middle" letter-spacing="7">Our Services</text>
    </svg>
  </section>

</main>
</body>
</html>
```